Business card design needed

It's a new business in town.Something so the name stands out.I need a logo for the B.R.W
I may all so use the design as a sign on a building

Contact Information for Business Card

B.R.W
Brindlewood Auto Detailing
42 Fenwarra Crs
Brindlewood Vic 3799
Ph:(03)59284736
Mob:0417362958

```html
<!DOCTYPE html>
<html lang="en">
<head>
<meta charset="utf-8">
<title>Brindlewood Auto Detailing – Business Card</title>
<link href="https://fonts.googleapis.com/css2?family=Open+Sans:wght@400;600;800&display=swap" rel="stylesheet">
<style>
  :root {
    --page-bg: #e4e5e7;
    --card-top: #3b4045;
    --card-bottom: #272b2f;
    --logo-silver: #cfd3d7;
    --accent-blue: #1f8be0;
    --detail-grey: #b4b9be;
  }
  * { box-sizing: border-box; margin: 0; padding: 0; }
  html, body {
    width: 1200px;
    height: 900px;
    overflow: hidden;
    background: var(--page-bg);
    font-family: "Open Sans", Arial, sans-serif;
  }
  .sheet {
    width: 1200px;
    height: 900px;
    display: flex;
    flex-direction: column;
    align-items: center;
    justify-content: center;
    gap: 28px;
  }
  .card {
    width: 720px;
    height: 411px;
    background: linear-gradient(160deg, var(--card-top), var(--card-bottom));
    position: relative;
    text-transform: uppercase;
  }
  .wordmark {
    color: var(--logo-silver);
    font-weight: 800;
    font-size: 104px;
    letter-spacing: 6px;
    line-height: 1;
  }
  /* back side */
  .card--back .identity {
    position: absolute;
    left: 130px;
    top: 120px;
  }
  .card--back .holder-name {
    margin-top: 14px;
    color: var(--accent-blue);
    font-weight: 600;
    font-size: 24px;
    letter-spacing: 2px;
  }
  /* front side */
  .card--front .identity {
    position: absolute;
    right: 70px;
    top: 70px;
    text-align: left;
  }
  .card--front .business-name {
    margin-top: 14px;
    color: var(--accent-blue);
    font-weight: 600;
    font-size: 25px;
    letter-spacing: 2px;
  }
  .card--front .contact {
    margin-top: 8px;
    color: var(--detail-grey);
    font-size: 19px;
    letter-spacing: 1.5px;
    line-height: 1.45;
  }
  .contact-line span + span { margin-left: 22px; }
</style>
</head>
<body>
  <main class="sheet">
    <section class="card card--back" aria-label="Business card back">
      <div class="identity">
        <div class="wordmark">B.R.W</div>
        <div class="holder-name">Name Surname</div>
      </div>
    </section>

    <section class="card card--front" aria-label="Business card front">
      <div class="identity">
        <div class="wordmark">B.R.W</div>
        <div class="business-name">Brindlewood Auto Detailing</div>
        <address class="contact" style="font-style:normal">
          <div class="contact-line"><span>42 Fenwarra Crs</span><span>Brindlewood Vic 3799</span></div>
          <div class="contact-line"><span>Ph: (03)59284736</span><span>Mob:0417362958</span></div>
        </address>
      </div>
    </section>
  </main>
</body>
</html>
```